Quorvane - New design for a couple of our pages

We need a total renovation of one of our webpages. First we would like the "insight and analysis" to be redesigned- for now we think the page is ok, but we want it to be great. We want this design to

We specialize in business intelligence and business management software. We are open for removal of some of the text on the site. Generally, we want the page to reflect that we are a modern technology company. See the frontpage of the website for common colors, however, we are open for better ones. We also need the design implemented on our site. If the page becomes a success, then there is a good chance that we would like a similar design for the other pages as well.Se link for the page that we need improved:https://www.quorvane.example/project/innsikt-og-analyse/?lang=en

Our main page also needs to be improved, here you will find our color palette, we would like more modern colors.

Sites we want to see with the new design suggestion:

Main page:
https://www.quorvane.example/

about us:
https://www.quorvane.example/aboutus/?lang=en

Finance and planning:
https://www.quorvane.example/project/finance-and-planning/?lang=en

Retail:
https://www.quorvane.example/project/retail/?lang=en

Target Market(s)

30 + / Business oriented / Desicion makers / financial officers / Educated

Industry/Entity Type

Information Technology

Number of Pages Required

5+ page

Font styles to use
Sans Serif

Requirements
Must have
• - Overall, we want the page to trigger the visitor to call us and schedule a meeting.
Nice to have
• Nice to have a sugguestion for a call to action - e.g. contact form. We are open to remove text and add another level of paiges under this one - again, open for suggestions for the content as well.
• We want similar colors to the already used greens and blue shades - but the designer may improble the color selection. Perhaps the designer can suggest a few options.

```html
<!DOCTYPE html>
<html lang="en">
<head>
<meta charset="utf-8">
<title>Quorvane – Insights and Analytics</title>
<link href="https://fonts.googleapis.com/css2?family=Montserrat:wght@500;600;700;800&family=Open+Sans:wght@400;600;700&display=swap" rel="stylesheet">
<style>
:root{
  --teal-deep:#0c4f52;
  --teal:#17706c;
  --teal-mid:#1f8a80;
  --teal-bright:#2fb3a3;
  --teal-soft:#d8ecea;
  --mint:#e9f5f3;
  --navy:#1d2a5c;
  --ink:#13393b;
  --text:#3b4a4b;
  --white:#ffffff;
  --line:#9fc9c4;
}
*{box-sizing:border-box;margin:0;padding:0}
html,body{width:1200px;height:4534px;overflow:hidden}
body{position:relative;background:var(--white);font-family:"Open Sans",Arial,sans-serif;color:var(--text)}
.abs{position:absolute}
h1,h2,h3,.brand,.btn{font-family:"Montserrat",Arial,sans-serif}
.brand{font-weight:800;font-size:40px;color:var(--ink);letter-spacing:-1px;display:flex;align-items:center;gap:10px}
.brand .dot{width:12px;height:12px;background:var(--teal-bright);border-radius:50%}
.nav{display:flex;gap:22px;font-size:15px;font-weight:400;font-family:"Open Sans",Arial,sans-serif}
.nav a{color:var(--ink);text-decoration:none;white-space:nowrap}
.lang{width:60px;height:30px;border:2px solid var(--white);border-radius:3px;background:rgba(255,255,255,.15);display:flex;align-items:center;justify-content:center;gap:6px}
.lang span{width:22px;height:14px;background:#c9d6e8}
.btn{display:flex;align-items:center;justify-content:center;border:3px solid var(--teal-mid);color:var(--teal);font-weight:700;font-size:15px;letter-spacing:.5px;text-transform:uppercase;background:var(--white)}
.btn.light{border-color:var(--white);color:var(--white);background:transparent}
.dash{display:flex;gap:6px;margin:10px 0 18px}
.dash i{display:block;width:14px;height:4px;background:var(--teal-bright)}
.dash.center{justify-content:center}
h2{font-size:31px;font-weight:700;color:var(--ink)}
.on-dark h2{color:var(--white)}
.body{font-size:15.5px;line-height:1.55}
.on-dark .body{color:#e3f1ef}
.art{border-radius:6px}
.card{position:absolute;background:var(--white);box-shadow:0 6px 18px rgba(12,79,82,.18);text-align:center;padding:28px 18px 0}
.card h3{font-size:21px;color:var(--teal);font-weight:700;margin:10px 0 8px;line-height:1.1}
.card p{font-size:13.5px;line-height:1.35;color:var(--text)}
.card .chev{width:36px;height:36px;border:2px solid var(--teal-mid);border-radius:50%;margin:14px auto 0;display:flex;align-items:center;justify-content:center}
.card.featured{background:var(--teal);}
.card.featured h3,.card.featured p{color:var(--white)}
.card.featured .chev{border-color:#0a3436}
.field{position:absolute;border:1.5px solid var(--line);background:var(--white);font-size:15px;color:var(--text);padding:12px 20px}
.submit{position:absolute;background:var(--teal);color:var(--white);font-family:"Montserrat",Arial,sans-serif;font-weight:700;font-size:15px;display:flex;align-items:center;justify-content:center;text-transform:uppercase}
.foot h4{font-family:"Montserrat",Arial,sans-serif;font-size:17px;color:var(--teal);font-weight:700;margin-bottom:12px}
.foot li{list-style:none;font-size:15px;line-height:1.75;color:var(--ink)}
.social li{display:flex;align-items:center;gap:10px;line-height:2.2}
.social b{width:22px;height:22px;border-radius:50%;background:#2a7fb0;display:inline-block}
</style>
</head>
<body>

<section class="hero">
  <div class="abs" style="left:0;top:0;width:1200px;height:600px;background:linear-gradient(180deg,#f4faf9,#e6f2f0)"></div>
  <svg class="abs" style="left:0;top:0" width="1200" height="640" viewBox="0 0 1200 640">
    <defs>
      <linearGradient id="heroWave" x1="0" y1="1" x2="1" y2="0">
        <stop offset="0" stop-color="#1f8a80"/><stop offset=".5" stop-color="#17706c"/><stop offset="1" stop-color="#0c4f52"/>
      </linearGradient>
    </defs>
    <path d="M0,575 C300,560 560,520 700,330 C790,200 830,60 880,0 L1200,0 L1200,600 L0,600 Z" fill="url(#heroWave)"/>
    <path d="M0,600 C400,590 800,560 1200,520 L1200,640 L0,640 Z" fill="#ffffff"/>
  </svg>
  <div class="abs brand" style="left:157px;top:28px">Quorvane<span class="dot"></span></div>
  <nav class="abs nav" style="left:418px;top:43px"><a>Industries</a><a>Solutions</a><a>Courses</a><a>Customers</a><a>About Us</a></nav>
  <svg class="abs" style="left:902px;top:42px" width="22" height="22" viewBox="0 0 22 22"><circle cx="9" cy="9" r="7" fill="none" stroke="#fff" stroke-width="2.5"/><line x1="14" y1="14" x2="20" y2="20" stroke="#fff" stroke-width="2.5"/></svg>
  <div class="abs lang" style="left:980px;top:38px"><span></span><svg width="10" height="6" viewBox="0 0 10 6"><path d="M1 1l4 4 4-4" stroke="#fff" fill="none" stroke-width="1.6"/></svg></div>

  <h1 class="abs" style="left:157px;top:176px;font-size:45px;font-weight:800;color:var(--teal-deep)">Insights and Analytics</h1>
  <p class="abs" style="left:157px;top:232px;font-family:Montserrat,Arial,sans-serif;font-size:26px;font-weight:700;color:var(--ink)">Accurate Information Faster</p>
  <p class="abs body" style="left:157px;top:280px;width:440px;font-size:16px;color:var(--ink)">Maecenas aliquet velit vel turpis Mauris neque metus malesuada nec ultricies sit amet porttitor</p>
  <div class="abs btn" style="left:157px;top:356px;width:184px;height:49px">Contact Us</div>

  <div class="abs art" role="img" aria-label="Isometric illustration of a tablet with glowing analytics charts and a data server stack" style="left:635px;top:95px;width:483px;height:390px;background:radial-gradient(ellipse at 55% 55%,#6fd6e8 0%,#3a7fc8 40%,rgba(40,70,160,.55) 65%,rgba(23,112,108,0) 80%)"></div>

  <div class="abs" style="left:566px;top:518px;display:flex;gap:10px">
    <span style="width:14px;height:14px;border:2px solid #fff;border-radius:50%"></span>
    <span style="width:14px;height:14px;background:#fff;border-radius:50%"></span>
    <span style="width:14px;height:14px;border:2px solid #fff;border-radius:50%"></span>
  </div>
</section>

<section class="value">
  <div class="abs" style="left:124px;top:698px;width:446px;height:290px;border:1.5px solid #c9d3e6"></div>
  <div class="abs art" role="img" aria-label="Explainer video still with an animated presenter" style="left:136px;top:685px;width:444px;height:287px;border-radius:0;background:linear-gradient(135deg,#b9d9ec,#7fb0d4 55%,#5d4a3b)"></div>
  <svg class="abs" style="left:322px;top:786px" width="70" height="70" viewBox="0 0 70 70"><circle cx="35" cy="35" r="33" fill="#fff"/><path d="M28 22 L50 35 L28 48 Z" fill="#13393b"/></svg>

  <h2 class="abs" style="left:622px;top:692px;font-size:29px">More value of your data</h2>
  <div class="abs dash" style="left:622px;top:724px"><i></i><i></i><i></i></div>
  <p class="abs body" style="left:622px;top:756px;width:420px;font-size:14.5px">Quorvane provides you with the insight that you need to take the nessesary descions that will give your company increased  value and growth. I Quorvane er vi opptatt av å kombinere det beste teknologien med dyp bransjekunnskap og forretningsforståelse.</p>
  <div class="abs btn" style="left:626px;top:904px;width:184px;height:48px">Learn More</div>
</section>

<section class="band on-dark">
  <svg class="abs" style="left:0;top:1090px" width="1200" height="1270" viewBox="0 0 1200 1270">
    <defs>
      <linearGradient id="bandFill" x1="0" y1="0" x2="1" y2="1">
        <stop offset="0" stop-color="#1a8078"/><stop offset=".45" stop-color="#0f5c5a"/><stop offset="1" stop-color="#0c4f52"/>
      </linearGradient>
    </defs>
    <path d="M0,40 C300,20 700,60 1200,10 L1200,1190 C900,1230 500,1240 0,1200 Z" fill="url(#bandFill)"/>
    <path d="M0,1200 C500,1240 900,1230 1200,1190 L1200,1270 C800,1215 400,1250 0,1230 Z" fill="#1f8a80" opacity=".6"/>
  </svg>

  <h2 class="abs" style="left:164px;top:1222px">Dashboard og Reporting</h2>
  <div class="abs dash" style="left:164px;top:1256px"><i></i><i></i><i></i></div>
  <p class="abs body" style="left:164px;top:1290px;width:420px;font-size:14.5px">With Quorvane Frontline and 3rd party tools like Nordsoft Vista BI, Quorvane provides you and your organization fast and easy access to key figures and management information whenever, wherever, no training required. The end user and decision-makers gain access</p>
  <div class="abs btn light" style="left:165px;top:1438px;width:184px;height:48px">Learn More</div>
  <div class="abs art" role="img" aria-label="Dark dashboard screen with gauges, donut charts and a line chart" style="left:658px;top:1178px;width:322px;height:296px;border-radius:0;background:linear-gradient(160deg,#2a2f6e,#151a44)"></div>

  <div class="abs" role="img" aria-label="Isometric illustration of stacked glowing data warehouse blocks" style="left:181px;top:1555px;width:378px;height:287px;background:radial-gradient(ellipse at 50% 50%,#4fe0c8 0%,#2a4fa0 45%,rgba(15,92,90,0) 72%)"></div>
  <h2 class="abs" style="left:634px;top:1578px">Datawarehouse</h2>
  <div class="abs dash" style="left:634px;top:1612px"><i></i><i></i><i></i></div>
  <p class="abs body" style="left:634px;top:1646px;width:420px;font-size:14.5px">In Quorvane we are experts in data warehouses on the Nordsoft platform, and we provide solutions to a wide range of Norwegian and international customers. By combining our experience of system integration with metadata-based ETL (Extract, Transform and Load), we accelerate the development, deployment,</p>
  <div class="abs btn light" style="left:637px;top:1810px;width:184px;height:48px">Learn More</div>

  <h2 class="abs" style="left:175px;top:1962px">Advanced analytics</h2>
  <div class="abs dash" style="left:175px;top:1996px"><i></i><i></i><i></i></div>
  <p class="abs body" style="left:175px;top:2030px;width:420px;font-size:14.5px">In Quorvane we are experts in data warehouses on the Nordsoft platform, and we provide solutions to a wide range of Norwegian and international customers. By combining our experience of system integration with metadata-based ETL (Extract, Transform and Load), we accelerate the development, deployment,</p>
  <div class="abs btn light" style="left:176px;top:2198px;width:184px;height:48px">Learn More</div>
  <div class="abs" role="img" aria-label="Isometric illustration of an analyst standing on a platform among holographic charts" style="left:664px;top:1872px;width:357px;height:393px;background:radial-gradient(ellipse at 50% 55%,#c7e6ff 0%,#4a6cc8 40%,rgba(12,79,82,0) 72%)"></div>
</section>

<section class="solutions">
  <div class="abs" style="left:0;top:2360px;width:1200px;height:540px;background:linear-gradient(180deg,#e2f1ef,#ffffff)"></div>
  <h2 class="abs" style="left:0;top:2430px;width:1200px;text-align:center;color:var(--teal);font-size:30px">Solutions and Services</h2>
  <div class="abs dash center" style="left:0;top:2464px;width:1200px"><i></i><i></i><i></i></div>

  <div class="card featured" style="left:157px;top:2510px;width:205px;height:253px">
    <svg width="64" height="56" viewBox="0 0 64 56"><path d="M18 40 H14 a11 11 0 0 1 0-22 a16 16 0 0 1 31-4 a12 12 0 0 1 5 26 h-4" fill="none" stroke="#fff" stroke-width="2.5"/><path d="M32 26 v26 M25 33 l7-7 7 7" stroke="#fff" stroke-width="2.5" fill="none"/></svg>
    <h3>Cloud</h3>
    <p>Maecenas aliquet velit vel turpis Mauris neque metus malesuad</p>
    <div class="chev"><svg width="14" height="9" viewBox="0 0 14 9"><path d="M1 1l6 6 6-6" stroke="#0a3436" stroke-width="2" fill="none"/></svg></div>
  </div>
  <div class="card" style="left:384px;top:2582px;width:202px;height:257px">
    <svg width="64" height="56" viewBox="0 0 64 56"><rect x="16" y="6" width="40" height="34" fill="none" stroke="#17706c" stroke-width="2.5"/><path d="M22 32 l10-10 8 6 10-12" stroke="#17706c" stroke-width="2.5" fill="none"/><rect x="6" y="36" width="16" height="14" fill="none" stroke="#17706c" stroke-width="2.5"/></svg>
    <h3>Finance &amp;<br>Planning</h3>
    <p>Maecenas aliquet velit vel turpis Mauris</p>
    <div class="chev"><svg width="14" height="9" viewBox="0 0 14 9"><path d="M1 1l6 6 6-6" stroke="#1f8a80" stroke-width="2" fill="none"/></svg></div>
  </div>
  <div class="card" style="left:610px;top:2510px;width:205px;height:253px">
    <svg width="64" height="56" viewBox="0 0 64 56"><rect x="8" y="6" width="48" height="36" fill="none" stroke="#17706c" stroke-width="2.5"/><path d="M20 34v-10M28 34V16M36 34v-14M44 34V12" stroke="#17706c" stroke-width="3"/><path d="M24 50h16M32 42v8" stroke="#17706c" stroke-width="2.5"/></svg>
    <h3>Reporting</h3>
    <p>Maecenas aliquet velit vel turpis Mauris</p>
    <div class="chev"><svg width="14" height="9" viewBox="0 0 14 9"><path d="M1 1l6 6 6-6" stroke="#1f8a80" stroke-width="2" fill="none"/></svg></div>
  </div>
  <div class="card" style="left:836px;top:2582px;width:206px;height:257px">
    <svg width="64" height="56" viewBox="0 0 64 56"><rect x="8" y="6" width="48" height="36" fill="none" stroke="#17706c" stroke-width="2.5"/><circle cx="32" cy="24" r="9" fill="none" stroke="#17706c" stroke-width="2.5"/><circle cx="32" cy="24" r="3" fill="#17706c"/><path d="M24 50h16M32 42v8" stroke="#17706c" stroke-width="2.5"/></svg>
    <h3>Software</h3>
    <p>Maecenas aliquet velit vel turpis Mauris</p>
    <div class="chev"><svg width="14" height="9" viewBox="0 0 14 9"><path d="M1 1l6 6 6-6" stroke="#1f8a80" stroke-width="2" fill="none"/></svg></div>
  </div>
</section>

<section class="suite">
  <div class="abs" role="img" aria-label="Isometric illustration of cloud services connected to a central processing cube" style="left:136px;top:2914px;width:438px;height:348px;background:radial-gradient(ellipse at 50% 50%,#7fe0d2 0%,#2fb3a3 40%,rgba(255,255,255,0) 72%)"></div>
  <h2 class="abs" style="left:619px;top:2944px">Aurelis Intelligence Suite</h2>
  <div class="abs dash" style="left:619px;top:2978px"><i></i><i></i><i></i></div>
  <p class="abs body" style="left:619px;top:3010px;width:420px;font-size:14.5px">Aurelis Intelligence Suite (AIS) is an umbrella term for a series of cloud services and APIs, provided by Nordsoft, for building, modelling and presentation of Big Data solutions, and for giving new insights in the form of predictive and prescriptive analysis.</p>
  <div class="abs btn" style="left:621px;top:3158px;width:184px;height:48px">Learn More</div>
</section>

<section class="bi">
  <svg class="abs" style="left:0;top:3280px" width="1200" height="440" viewBox="0 0 1200 440">
    <defs>
      <linearGradient id="biWave" x1="0" y1="1" x2="1" y2="0">
        <stop offset="0" stop-color="#2fb3a3"/><stop offset=".5" stop-color="#17706c"/><stop offset="1" stop-color="#0c4f52"/>
      </linearGradient>
    </defs>
    <path d="M380,430 C700,420 900,380 1020,240 C1090,150 1140,70 1200,30 L1200,440 L380,440 Z" fill="url(#biWave)"/>
    <path d="M250,440 C650,428 1000,400 1200,350 L1200,440 Z" fill="#ffffff"/>
  </svg>
  <h2 class="abs" style="left:166px;top:3356px">Vista BI</h2>
  <div class="abs dash" style="left:166px;top:3390px"><i></i><i></i><i></i></div>
  <p class="abs body" style="left:166px;top:3422px;width:420px;font-size:14.5px">Aurelis Intelligence Suite (AIS) is an umbrella term for a series of cloud services and APIs, provided by Nordsoft, for building, modelling and presentation of Big Data solutions, and for giving new insights in the form of predictive and prescriptive analysis.</p>
  <div class="abs btn" style="left:170px;top:3571px;width:184px;height:48px">Learn More</div>
  <div class="abs" role="img" aria-label="Isometric illustration of a robot assistant rising from a tablet" style="left:649px;top:3262px;width:393px;height:362px;background:radial-gradient(ellipse at 50% 55%,#7fa8ff 0%,#3a4fb8 40%,rgba(29,42,92,0) 72%)"></div>
</section>

<section class="contact">
  <div class="abs" style="left:0;top:3820px;width:1200px;height:330px;background:linear-gradient(180deg,#ffffff,#eef6f5)"></div>
  <h2 class="abs" style="left:0;top:3750px;width:1200px;text-align:center;color:var(--teal);font-size:30px">Contact Form</h2>
  <div class="abs dash center" style="left:0;top:3784px;width:1200px"><i></i><i></i><i></i></div>
  <div class="field" style="left:202px;top:3830px;width:387px;height:46px">Your Name</div>
  <div class="field" style="left:202px;top:3886px;width:387px;height:46px">Email address</div>
  <div class="field" style="left:202px;top:3941px;width:387px;height:46px">Phone Number</div>
  <div class="field" style="left:604px;top:3830px;width:387px;height:157px">Message</div>
  <div class="submit" style="left:504px;top:4014px;width:185px;height:42px">Submit Now</div>
</section>

<footer class="foot">
  <svg class="abs" style="left:0;top:4120px" width="1200" height="120" viewBox="0 0 1200 120">
    <path d="M0,30 C300,70 700,80 1200,0 L1200,50 C800,110 350,100 0,80 Z" fill="#8fd3c8"/>
    <path d="M0,50 C350,100 800,110 1200,30 L1200,120 L0,120 Z" fill="#ffffff"/>
  </svg>
  <div class="abs brand" style="left:187px;top:4222px">Quorvane<span class="dot"></span></div>
  <div class="abs" style="left:462px;top:4222px">
    <h4>QUICK LINKS</h4>
    <ul><li>Industries</li><li>Solutions</li><li>Courses</li><li>Customers</li><li>About Us</li></ul>
  </div>
  <div class="abs" style="left:634px;top:4222px">
    <h4>CONTACT US</h4>
    <ul><li>EIRIK SOLVANG</li><li>T: +47 91 23 45 67</li><li>E: eirik.solvang@quorvane.example</li></ul>
  </div>
  <div class="abs social" style="left:894px;top:4222px">
    <h4>FOLLOW US</h4>
    <ul><li><b></b>Chatter</li><li><b></b>Friendwall</li><li><b></b>ProNet</li></ul>
  </div>
  <div class="abs" style="left:157px;top:4458px;width:886px;height:1px;background:#c3d2d1"></div>
  <p class="abs" style="left:0;top:4482px;width:1200px;text-align:center;font-size:14px;color:var(--ink)">© 2019 Company Name  All right reserved</p>
</footer>

</body>
</html>
```